iOS7 test prep app

I need 3 basic screens and 2 product images for an iOS7 app I am prototyping. I provided lots of detail in the attached brief. This is an education product, so warm colors (especially reds) work best.

If you've done flat design for mobile products, please take a look ... Thanks!

Greetings, all. Thank you for your submissions. I am meeting with my product development team this week to review your submissions, and will select a designer before the end of the week. I appreciate your patience with my process, and thank you again for your interest in my project. I'll be back to you soon ... -Gordon

```html
<!DOCTYPE html>
<html lang="en">
<head>
<meta charset="utf-8">
<title>Test Prep Dashboard</title>
<link rel="stylesheet" href="https://fonts.googleapis.com/css2?family=Roboto:ital,wght@0,300;0,400;0,500;0,700;1,400;1,700;1,900&display=swap">
<style>
  :root{
    --status-bg:#4b4b4b;
    --header-bg:#f8c3a3;
    --accent:#f0894a;
    --page-bg:#f6f3f3;
    --card-bg:#ffffff;
    --card-head:#d6d6d6;
    --card-head-line:#bcbcbc;
    --label:#6b6b6b;
    --value:#444444;
    --rule:#e6e6e6;
    --yellow:#f6c400;
    --red:#e8431e;
    --green:#48ab22;
    --gauge-rest:#f1f1f1;
    --needle:#5a5a5a;
  }
  *{box-sizing:border-box;margin:0;padding:0}
  html,body{width:768px;height:1200px;overflow:hidden}
  body{background:var(--page-bg);font-family:"Roboto",Helvetica,Arial,sans-serif;color:var(--value)}
  .screen{position:relative;width:768px;height:1200px}

  .status-bar{height:40px;background:var(--status-bg);color:#fff;display:flex;align-items:center;justify-content:space-between;padding:0 16px;font-size:20px;font-weight:400}
  .status-left,.status-right{display:flex;align-items:center;gap:8px;width:240px}
  .status-right{justify-content:flex-end}
  .signal{display:flex;gap:3px}
  .signal i{width:12px;height:12px;border-radius:50%;background:#fff;display:block}
  .signal i.off{background:none;border:1.5px solid #fff}

  .app-header{height:72px;background:var(--header-bg);border-bottom:4px solid var(--accent);display:flex;align-items:stretch}
  .header-btn{width:74px;display:flex;align-items:center;justify-content:center}
  .header-btn.menu{border-right:1px solid #eaa37c}
  .header-btn.logout{width:70px;border-left:1px solid #eaa37c}
  .header-title{flex:1;display:flex;align-items:center;justify-content:center;color:#fff;font-style:italic;font-weight:700;font-size:20px;letter-spacing:2.5px;text-transform:uppercase}

  .dashboard{position:absolute;left:26px;right:26px;top:154px}
  .card-grid{display:grid;grid-template-columns:346px 346px;column-gap:24px;row-gap:22px}
  .card{background:var(--card-bg);border-radius:6px;overflow:hidden;height:274px}
  .card.wide{grid-column:1 / 3;height:276px}
  .card-head{height:50px;background:var(--card-head);border-bottom:3px solid var(--card-head-line);display:flex;align-items:center;padding-left:18px;color:#fff;font-style:italic;font-weight:900;font-size:14px;letter-spacing:1.6px;text-transform:uppercase}

  .stat-list{list-style:none;padding:8px 18px 0 24px}
  .stat-row{height:49px;display:flex;align-items:center;border-bottom:1px solid var(--rule);font-size:21px}
  .stat-row:last-child{border-bottom:none}
  .stat-label{flex:1;font-weight:300;color:var(--label)}
  .stat-value{font-weight:700;font-size:20px}
  .stat-value.plain{color:var(--value)}
  .booster .stat-value{margin-right:34px}
  .trend-icon{width:28px;height:20px;margin-left:20px}
  .key-stats .trend-icon{margin-left:0}
  .yellow{color:var(--yellow)} .red{color:var(--red)} .green{color:var(--green)}

  .readiness{position:relative;text-align:center}
  .readiness-value{position:absolute;left:0;right:0;top:60px;font-size:40px;font-weight:500;color:var(--yellow);line-height:1}
  .gauge{position:absolute;left:23px;top:108px;width:300px;height:142px}
  .gauge-label{position:absolute;bottom:12px;font-size:13px;font-style:italic;font-weight:400;letter-spacing:.2px}
  .gauge-label.low{left:18px;color:var(--red)}
  .gauge-label.high{right:18px;color:var(--green)}

  .distribution{display:block;margin:14px auto 0;width:314px;height:200px}
  .distribution text{font-family:"Roboto",Helvetica,Arial,sans-serif;font-size:11px;fill:#666}

  .trend-columns{display:grid;grid-template-columns:1fr 1fr;column-gap:60px;padding:8px 18px 0 24px}
  .trend-columns .stat-list{padding:0}

  .begin-test{position:absolute;left:26px;right:26px;top:1065px;height:78px;border-radius:6px;background:var(--accent);color:#fff;display:flex;align-items:center;justify-content:center;gap:12px;font-weight:700;font-size:21px;letter-spacing:4px;text-transform:uppercase}
</style>
</head>
<body>
<div class="screen">
  <div class="status-bar">
    <div class="status-left">
      <span class="signal"><i></i><i></i><i></i><i></i><i class="off"></i></span>
      <span>Carrier</span>
      <svg width="22" height="16" viewBox="0 0 22 16"><path d="M2 6a13 13 0 0 1 18 0M5 9.5a8.5 8.5 0 0 1 12 0M8 13a4 4 0 0 1 6 0" fill="none" stroke="#fff" stroke-width="2.2" stroke-linecap="round"/></svg>
    </div>
    <span>5:30PM</span>
    <div class="status-right">
      <svg width="20" height="20" viewBox="0 0 20 20"><circle cx="10" cy="10" r="8.5" fill="none" stroke="#fff" stroke-width="1.6"/><rect x="6.5" y="9" width="7" height="5.5" fill="#fff"/><path d="M8 9V7.5a2 2 0 0 1 4 0V9" fill="none" stroke="#fff" stroke-width="1.5"/></svg>
      <span>100%</span>
      <svg width="58" height="22" viewBox="0 0 58 22"><rect x="1" y="1.5" width="51" height="19" rx="3" fill="none" stroke="#fff" stroke-width="1.6"/><rect x="3.5" y="4" width="46" height="14" rx="1.5" fill="#fff"/><rect x="53.5" y="7.5" width="3" height="7" rx="1" fill="#fff"/></svg>
    </div>
  </div>

  <header class="app-header">
    <div class="header-btn menu">
      <svg width="30" height="22" viewBox="0 0 30 22"><path d="M2 3h26M2 11h26M2 19h26" stroke="#fff" stroke-width="2.6" stroke-linecap="round"/></svg>
    </div>
    <h1 class="header-title">Welcome, Michael!</h1>
    <div class="header-btn logout">
      <svg width="30" height="30" viewBox="0 0 30 30"><path d="M20 10V4H4v22h16v-6" fill="none" stroke="#fff" stroke-width="2.4"/><path d="M12 15h15M22 10l5 5-5 5" fill="none" stroke="#fff" stroke-width="2.4" stroke-linejoin="round"/></svg>
    </div>
  </header>

  <main class="dashboard">
    <div class="card-grid">
      <section class="card key-stats">
        <h2 class="card-head">Key Stats</h2>
        <ul class="stat-list">
          <li class="stat-row"><span class="stat-label">Total Tests:</span><span class="stat-value plain">6</span></li>
          <li class="stat-row"><span class="stat-label">Last Score:</span><span class="stat-value yellow">68%</span></li>
          <li class="stat-row"><span class="stat-label">Cum. Score:</span><span class="stat-value red">59%</span></li>
          <li class="stat-row"><span class="stat-label">Trend:</span><svg class="trend-icon" viewBox="0 0 28 20"><polyline points="4,15 14,6 24,15" fill="none" stroke="var(--green)" stroke-width="4"/></svg></li>
        </ul>
      </section>

      <section class="card readiness">
        <h2 class="card-head">Readiness Meter</h2>
        <div class="readiness-value">58%</div>
        <svg class="gauge" viewBox="0 0 300 142" aria-label="Readiness 58 percent">
          <path d="M72.5 140 A77.5 77.5 0 0 1 227.5 140" fill="none" stroke="var(--gauge-rest)" stroke-width="65"/>
          <path d="M72.5 140 A77.5 77.5 0 0 1 169.3 64.9" fill="none" stroke="var(--yellow)" stroke-width="65"/>
          <line x1="150" y1="139" x2="178" y2="28" stroke="var(--needle)" stroke-width="4.5" stroke-linecap="round"/>
        </svg>
        <span class="gauge-label low">NOT READY</span>
        <span class="gauge-label high">READY</span>
      </section>

      <section class="card booster">
        <h2 class="card-head">Booster Levels</h2>
        <ul class="stat-list">
          <li class="stat-row"><span class="stat-label">HP:</span><span class="stat-value plain">5X</span><svg class="trend-icon" viewBox="0 0 28 20"><polyline points="4,15 14,6 24,15" fill="none" stroke="var(--red)" stroke-width="4"/></svg></li>
          <li class="stat-row"><span class="stat-label">PI:</span><span class="stat-value plain">5X</span><svg class="trend-icon" viewBox="0 0 28 20"><polyline points="4,15 14,6 24,15" fill="none" stroke="var(--red)" stroke-width="4"/></svg></li>
          <li class="stat-row"><span class="stat-label">PA:</span><span class="stat-value plain">4X</span><svg class="trend-icon" viewBox="0 0 28 20"><polyline points="4,5 14,14 24,5" fill="none" stroke="var(--green)" stroke-width="4"/></svg></li>
          <li class="stat-row"><span class="stat-label">CM:</span><span class="stat-value plain">3X</span><svg class="trend-icon" viewBox="0 0 28 20"><polyline points="4,5 14,14 24,5" fill="none" stroke="var(--green)" stroke-width="4"/></svg></li>
        </ul>
      </section>

      <section class="card">
        <h2 class="card-head">Test Plan Distribution</h2>
        <svg class="distribution" viewBox="0 0 314 200" aria-label="Test plan distribution bar">
          <g fill="none" stroke="#b5b5b5" stroke-width="1">
            <path d="M22 74V18h16M77 74V30h16M134 74V42h16M182 74V54h16"/>
            <path d="M196 116v12h-12M213 116v24h-12M235 116v36h-12M272 116v48h-12"/>
          </g>
          <text x="42" y="21">PA: 14%</text>
          <text x="97" y="33">MC: 20%</text>
          <text x="154" y="45">RRP: 12%</text>
          <text x="202" y="57">P&amp;PT: 15%</text>
          <text x="180" y="131" text-anchor="end">BC&amp;C: 9%</text>
          <text x="197" y="143" text-anchor="end">PI: 9%</text>
          <text x="219" y="155" text-anchor="end">HP&amp;M: 9%</text>
          <text x="256" y="167" text-anchor="end">S&amp;IC: 12%</text>
          <rect x="0" y="74" width="44" height="42" fill="#a9cbef"/>
          <rect x="44" y="74" width="63" height="42" fill="#9fcdc6"/>
          <rect x="107" y="74" width="38" height="42" fill="#bcd96f"/>
          <rect x="145" y="74" width="47" height="42" fill="#fde872"/>
          <rect x="192" y="74" width="28" height="42" fill="#fcc800"/>
          <rect x="220" y="74" width="28" height="42" fill="#fbab50"/>
          <rect x="248" y="74" width="28" height="42" fill="#f99a97"/>
          <rect x="276" y="74" width="38" height="42" fill="#e6afd4"/>
        </svg>
      </section>

      <section class="card wide">
        <h2 class="card-head">Trending Performance by Category</h2>
        <div class="trend-columns">
          <ul class="stat-list">
            <li class="stat-row"><span class="stat-label">Care Mgt:</span><span class="stat-value yellow">68%</span><svg class="trend-icon" viewBox="0 0 28 20"><polyline points="4,5 14,14 24,5" fill="none" stroke="var(--red)" stroke-width="4"/></svg></li>
            <li class="stat-row"><span class="stat-label">Safety IC:</span><span class="stat-value yellow">68%</span><svg class="trend-icon" viewBox="0 0 28 20"><polyline points="4,15 14,6 24,15" fill="none" stroke="var(--green)" stroke-width="4"/></svg></li>
            <li class="stat-row"><span class="stat-label">HP&amp;M:</span><span class="stat-value red">59%</span><svg class="trend-icon" viewBox="0 0 28 20"><polyline points="4,15 14,6 24,15" fill="none" stroke="var(--green)" stroke-width="4"/></svg></li>
            <li class="stat-row"><span class="stat-label">PI:</span><span class="stat-value red">44%</span><svg class="trend-icon" viewBox="0 0 28 20"><polyline points="4,5 14,14 24,5" fill="none" stroke="var(--red)" stroke-width="4"/></svg></li>
          </ul>
          <ul class="stat-list">
            <li class="stat-row"><span class="stat-label">Basic C&amp;C:</span><span class="stat-value green">77%</span><svg class="trend-icon" viewBox="0 0 28 20"><polyline points="4,5 14,14 24,5" fill="none" stroke="var(--red)" stroke-width="4"/></svg></li>
            <li class="stat-row"><span class="stat-label">Pharma PT:</span><span class="stat-value yellow">68%</span><svg class="trend-icon" viewBox="0 0 28 20"><polyline points="4,15 14,6 24,15" fill="none" stroke="var(--green)" stroke-width="4"/></svg></li>
            <li class="stat-row"><span class="stat-label">Risk:</span><span class="stat-value yellow">59%</span><svg class="trend-icon" viewBox="0 0 28 20"><polyline points="4,15 14,6 24,15" fill="none" stroke="var(--green)" stroke-width="4"/></svg></li>
            <li class="stat-row"><span class="stat-label">PA:</span><span class="stat-value red">44%</span><svg class="trend-icon" viewBox="0 0 28 20"><polyline points="4,5 14,14 24,5" fill="none" stroke="var(--red)" stroke-width="4"/></svg></li>
          </ul>
        </div>
      </section>
    </div>
  </main>

  <div class="begin-test">Begin Test
    <svg width="24" height="14" viewBox="0 0 24 14"><path d="M1 7h20M15 2l6 5-6 5" fill="none" stroke="#fff" stroke-width="2.2"/></svg>
  </div>
</div>
</body>
</html>
```